Anzeigengestaltung für Immobilienmakler für Wohnimmobilien
Zielgruppe
Immobilienmakler für Wohnimmobilien
Aufgabenstellung
Die Maße der Zeitungsanzeige sind 60 mm in der Höhe und 125 in der Breite, Dateiformat ist jpg oder Pdf mit 300dpi.
Bitte eines der zur Verfügung gestellten Logos verwenden
Folgender Text soll in der Anzeige enthalten sein:
Ihr kompetenter Immobilienmakler im Ennepe-Ruhr-Kreis
Lindenweg 7 - 45549 Sprockhövel
Tel. 0202 - 47315526 - www.wohnfeld.de
Optionaler zusätzlicher Text, falls noch Platz in der Anzeige ist:
Gerne bieten wir Ihnen ein unverbindliches Beratungsgespräch, sowie eine
kostenlose Wertermittlung an

```html
<!DOCTYPE html>
<html lang="de">
<head>
<meta charset="utf-8">
<title>Wohnfeld – Zeitungsanzeige</title>
<link href="https://fonts.googleapis.com/css2?family=Open+Sans:wght@400;700&display=swap" rel="stylesheet">
<style>
  :root {
    --page-bg: #ffffff;
    --ad-bg: #ffffff;
    --frame: #4a4a4a;
    --text-dark: #454749;
    --band: #4a4c4e;
    --band-text: #ffffff;
    --mark-grey: #a3a3a3;
    --divider: #9a9a9a;
    --photo-top: #8a7a66;
    --photo-mid: #b3a58e;
    --photo-bottom: #7d8a56;
  }
  html, body {
    margin: 0;
    padding: 0;
    width: 1200px;
    height: 846px;
    overflow: hidden;
    background: var(--page-bg);
    font-family: "Open Sans", Arial, sans-serif;
  }
  .ad {
    position: absolute;
    left: 242px;
    top: 250px;
    width: 705px;
    height: 336px;
    background: var(--ad-bg);
    border: 2px solid var(--frame);
    box-shadow: 0 1px 3px rgba(0,0,0,0.25);
    overflow: hidden;
  }
  .ad__photo {
    position: absolute;
    left: 0;
    top: 0;
    width: 307px;
    height: 100%;
    background: linear-gradient(180deg, var(--photo-top) 0%, var(--photo-mid) 55%, var(--photo-bottom) 100%);
  }
  .ad__headline {
    position: absolute;
    left: 331px;
    top: 24px;
    margin: 0;
    color: var(--text-dark);
    font-size: 29px;
    line-height: 34px;
    font-weight: 400;
    letter-spacing: 0.1px;
  }
  .ad__headline strong { font-weight: 700; }
  .ad__offer {
    position: absolute;
    left: 329px;
    top: 136px;
    width: 351px;
    height: 62px;
    box-sizing: border-box;
    padding: 10px 14px;
    background: var(--band);
    color: var(--band-text);
    font-size: 16px;
    line-height: 20px;
    margin: 0;
  }
  .brand {
    position: absolute;
    left: 330px;
    top: 222px;
    width: 160px;
    text-align: center;
  }
  .brand__mark {
    display: block;
    width: 50px;
    height: 50px;
    margin: 0 auto 10px;
    background: var(--mark-grey);
  }
  .brand__name {
    color: var(--text-dark);
    font-size: 20px;
    font-weight: 400;
    letter-spacing: 4px;
    text-transform: uppercase;
  }
  .ad__divider {
    position: absolute;
    left: 508px;
    top: 230px;
    width: 1px;
    height: 91px;
    background: var(--divider);
  }
  .contact {
    position: absolute;
    left: 531px;
    top: 240px;
    margin: 0;
    font-style: normal;
    color: var(--text-dark);
    font-size: 16px;
    line-height: 19.5px;
  }
  .contact__web { font-weight: 700; }
</style>
</head>
<body>
  <div class="ad">
    <div class="ad__photo" role="img" aria-label="Foto: Familie steht von hinten vor einem modernen Haus mit Garten"></div>

    <h1 class="ad__headline"><strong>Ihr kompetenter<br>Immobilienmakler</strong><br>im Ennepe-Ruhr-Kreis</h1>

    <p class="ad__offer">Unverbindliches Beratungsgespräch<br>und kostenlose Wertermittlung!</p>

    <div class="brand">
      <span class="brand__mark"></span>
      <div class="brand__name">Wohnfeld</div>
    </div>

    <div class="ad__divider"></div>

    <address class="contact">
      Lindenweg 7<br>
      45549 Sprockhövel<br>
      Tel. 0202/47315526<br>
      <span class="contact__web">www.wohnfeld.de</span>
    </address>
  </div>
</body>
</html>
```